Sticker design for prepared meals

I need 3 separate sticker designs for 3 categories of food - all of prepared meal types.
1. Traditional - needs to reflect traditional food/baking of old days Think rustic old style cooking. Maybe a checked table cloth. Maybe a sketch of someone baking with an oven etc.Needs to include our existing logo and wording "Ferdie's Traditional House Made Meals"
2. Takeaway - needs to reflect choice from popular takeaway cuisines - eg Chinese, Thai, Indian, Japanese. Needs to highlight choice - eg family of 4 can get what they want - not all the same cuisine etc. Words " Every family member gets to choose - top quality house made takeaway"
3. Fine Dining - needs to be classy and premium - eg black background with gold lettering - very pristine' very classy. Words include" Ferdie's Fine Dining at your home"
These will be for 3 separate types of stickers 80mm x 30 mm and I will need all files etc to pass onto the sticker company. Thanks

People interested in buying quality food and busy.

• As per project description

```html
<!DOCTYPE html>
<html lang="en">
<head>
<meta charset="utf-8">
<title>Ferdie's Meal Stickers</title>
<link rel="stylesheet" href="https://fonts.googleapis.com/css2?family=Kaushan+Script&family=Dancing+Script:wght@600;700&family=Montserrat:wght@400;800&family=Great+Vibes&display=swap">
<style>
  :root {
    --sky: #6ccbea;
    --check-light: #eeeeee;
    --check-blue: #8fd6ee;
    --white: #ffffff;
    --ink: #111111;
    --red: #e91d25;
    --charcoal: #303030;
    --gold-light: #fbe9a6;
    --gold: #e7bd45;
    --gold-deep: #d9a72c;
    --silver: #9a9a9a;
    --logo-navy: #2d2d7a;
  }
  * { box-sizing: border-box; margin: 0; padding: 0; }
  html, body { width: 1157px; height: 1200px; overflow: hidden; background: var(--white); }
  .canvas { position: relative; width: 1157px; height: 1200px; }

  .sticker { position: absolute; left: 269px; width: 619px; height: 232px; }
  .sticker > * { position: absolute; }

  .brand-mark {
    display: flex; align-items: center; justify-content: center; gap: 8px;
    font-family: "Montserrat", sans-serif; font-weight: 800; font-size: 19px;
    color: var(--logo-navy); white-space: nowrap;
  }
  .brand-mark .dot { width: 14px; height: 14px; border-radius: 50%; background: currentColor; flex: none; }

  /* Traditional */
  .sticker--traditional { top: 180px; background: var(--sky); }
  .sticker--traditional .inner { left: 22px; top: 22px; right: 22px; bottom: 22px; background: var(--white); }
  .sticker--traditional .tablecloth {
    left: 29px; top: 28px; width: 562px; height: 176px;
    background: linear-gradient(135deg, var(--check-blue), var(--check-light) 55%, var(--check-blue));
  }
  .sticker--traditional .brand-mark { left: 35px; top: 32px; width: 159px; height: 116px; }
  .sticker--traditional .stove {
    left: 455px; top: 26px; width: 132px; height: 178px;
    background: linear-gradient(180deg, #b9b9b3, #6f7466);
  }
  .headline {
    font-family: "Kaushan Script", cursive; color: var(--ink);
    white-space: nowrap; transform: translateX(-50%); line-height: 1;
  }
  .headline--name { left: 327px; top: 34px; font-size: 56px; }
  .headline--kind { left: 323px; top: 100px; font-size: 46px; }
  .headline--meals { left: 257px; top: 160px; font-size: 36px; }

  /* Takeaway */
  .sticker--takeaway { top: 484px; background: var(--red); }
  .sticker--takeaway .inner { left: 22px; top: 22px; right: 22px; bottom: 22px; background: var(--white); }
  .cuisine-list {
    left: 310px; top: 35px; transform: translateX(-50%); white-space: nowrap;
    font-family: "Montserrat", sans-serif; font-weight: 800; font-size: 20px; color: var(--ink);
  }
  .cuisine-list .sep { color: var(--red); margin: 0 4px; }
  .sticker--takeaway .brand-mark { left: 35px; top: 76px; width: 159px; height: 116px; }
  .tagline {
    font-family: "Dancing Script", cursive; font-weight: 700; color: var(--ink);
    white-space: nowrap; transform: translateX(-50%); line-height: 1; font-size: 30px;
  }
  .tagline--quality { left: 341px; top: 72px; }
  .tagline--made { left: 336px; top: 104px; }
  .takeaway-word {
    left: 339px; top: 136px; transform: translateX(-50%); white-space: nowrap; line-height: 1;
    font-family: "Dancing Script", cursive; font-weight: 700; font-size: 60px; color: var(--red);
  }
  .sticker--takeaway .chef {
    left: 463px; top: 68px; width: 128px; height: 132px;
    background: radial-gradient(circle at 50% 45%, #f4f4f4, #e6e6e6 70%, #ffffff);
  }

  /* Fine dining */
  .sticker--fine { top: 788px; background: linear-gradient(120deg, var(--gold-deep), var(--gold-light) 30%, var(--gold) 55%, var(--gold-light) 80%, var(--gold-deep)); }
  .sticker--fine .inner { left: 19px; top: 20px; width: 580px; height: 192px; background: var(--charcoal); }
  .sticker--fine .brand-mark { left: 38px; top: 32px; width: 165px; height: 124px; color: var(--gold); }
  .sticker--fine .table-setting {
    left: 298px; top: 32px; width: 217px; height: 112px;
    background: linear-gradient(90deg, #4a4a4a, #6a6a6a 50%, #4a4a4a);
  }
  .fine-line {
    left: 45px; top: 158px; display: flex; align-items: baseline; gap: 10px; white-space: nowrap;
    color: var(--white);
  }
  .fine-line .owner { font-family: "Montserrat", sans-serif; font-size: 31px; }
  .fine-line .script { font-family: "Great Vibes", cursive; font-size: 44px; }
  .fine-line .joiner { font-family: "Montserrat", sans-serif; font-size: 22px; color: var(--silver); }
</style>
</head>
<body>
<main class="canvas">

  <section class="sticker sticker--traditional">
    <div class="inner"></div>
    <div class="tablecloth" role="img" aria-label="Blue and white checked tablecloth"></div>
    <div class="brand-mark"><span class="dot"></span>Ferdie's Corner Deli</div>
    <h1 class="headline headline--name">Ferdie's</h1>
    <p class="headline headline--kind">Traditional</p>
    <p class="headline headline--meals">Home Made Meals</p>
    <div class="stove" role="img" aria-label="Old iron wood stove with hanging pots and kettles"></div>
  </section>

  <section class="sticker sticker--takeaway">
    <div class="inner"></div>
    <p class="cuisine-list"><span class="sep">·</span>CHINESE <span class="sep">·</span> THAI <span class="sep">·</span> INDIAN <span class="sep">·</span> JAPANESE <span class="sep">·</span></p>
    <div class="brand-mark"><span class="dot"></span>Ferdie's Corner Deli</div>
    <p class="tagline tagline--quality">Top Quality</p>
    <p class="tagline tagline--made">Home Made</p>
    <p class="takeaway-word">Takeaway</p>
    <div class="chef" role="img" aria-label="Cartoon sushi chef holding chopsticks and a roll"></div>
  </section>

  <section class="sticker sticker--fine">
    <div class="inner"></div>
    <div class="brand-mark"><span class="dot"></span>Ferdie's Corner Deli</div>
    <div class="table-setting" role="img" aria-label="White cutlery and plate table setting icons"></div>
    <p class="fine-line">
      <span class="owner">Ferdie's</span>
      <span class="script">Fine Dining</span>
      <span class="joiner">at</span>
      <span class="script">your home</span>
    </p>
  </section>

</main>
</body>
</html>
```